Online Prescription Eyeglass Lens Company Needs a Website

*Update new name to Glintwell. Thx

We are eye doctors with a lab that need a website for a new company based in Southern California called Glintwell. We replace old prescription lenses with new ones next day for most lenses. Patients select the lenses and give us the prescription. We then send a box with a prepaid shipping label. Place the frames in the box and drop them in the mail to our lab. We will custom make new lenses, fit them back into your frames and send them back to you. We would like to compete with www.spectrafold.com and offer affordable lenses for single vision, bifocal, progressive, sunglass lenses at an affordable price with next day shipping.
Updates

Hi Designers, We have a new name called Glintwell. Can we have the website design reflect the new name and we'll pick our favorites. Thx

Update: The new name is Brightmoor . I have not made very many changes or feedback to the submissions because we were bidding for a .com. We won and our new name is Brightmoor . This is the last name change.. Please have the website reflect the new name and I'll be providing feedback on the websites . ( I have a separate project for the logo people are working on, so don't worry about creating a logo). Look forward to the submissions. Thanks everyone.

Hi, Just leave the name as Glintwell for now. I will narrow down top designs tonight. Thx

Target Market(s)

Anyone that wears prescription or nonprescription glasses or sunglasses that want next day shipping.

Industry/Entity Type

Eyewear

Number of Pages Required

4 page

Font styles to use
Serif

Colors

Designer to choose colors to be used in the design.

Requirements
Must have
• I need a website that can compete with https://www.spectrafold.com/.
• We are different from spectrafold because we can offer same day service or next day shipping.
• It needs to have website that offers the lenses available listed below.
• Needs to be able to upload a prescription and payment feature.
• Pictures of different types of options with small info about each lens option.
• Template Pricing (just use numbers from $79-$179 for now)
• SINGLE VISION LENSES
• HIGH INDEX LENSES
• READING LENSES
• DIGITAL HD PROGRESSIVE LENSES
• RX & NON-RX SUNGLASSES
• RX & NON-RX POLARIZED SUNGLASSES
• COMPUTER LENSES
• TRANSITION LENSES
• BI-FOCAL LENSES

```html
<!DOCTYPE html>
<html lang="en">
<head>
<meta charset="utf-8">
<title>Glintwell — Prescription Lenses</title>
<link rel="stylesheet" href="https://fonts.googleapis.com/css2?family=Oswald:wght@400;500&family=Roboto:wght@400;500;700&family=Lora:wght@400&display=swap">
<style>
:root{
  --blue:#1f93ea;
  --slate:#5a626b;
  --slate-dark:#4a5058;
  --navy:#0b2240;
  --footer-bar:#5f6770;
  --text:#333a40;
  --muted:#666c72;
  --line:#d9dde1;
  --white:#ffffff;
}
*{margin:0;padding:0;box-sizing:border-box}
html,body{width:1200px;height:3435px;overflow:hidden}
body{position:relative;background:var(--white);font-family:"Roboto",Arial,sans-serif;color:var(--text)}
.abs{position:absolute}
.btn{position:absolute;display:flex;align-items:center;justify-content:center;font-family:"Roboto",sans-serif;font-weight:500;text-transform:uppercase;color:var(--white);background:var(--blue);border-radius:3px;font-size:14px;letter-spacing:.2px}

/* header */
.site-header{position:absolute;left:0;top:0;width:1200px;height:115px;background:var(--white)}
.phone-icon{left:87px;top:36px;width:44px;height:44px;border:1px solid var(--line);border-radius:50%;display:flex;align-items:center;justify-content:center}
.phone-number{left:155px;top:48px;font-size:19px;color:var(--text)}
.brand{left:0;width:1200px;top:52px;text-align:center;font-family:"Roboto",sans-serif;font-weight:700;font-size:36px;letter-spacing:3px;color:var(--slate-dark)}
.login{left:811px;top:54px;font-size:16px;font-weight:500;color:var(--text)}
.header-order{left:877px;top:41px;width:137px;height:41px;font-size:15px}
.menu-icon{left:1049px;top:44px;width:64px}
.menu-icon span{display:block;height:5px;background:var(--slate-dark);border-radius:3px;margin-bottom:8px}
.menu-icon span:nth-child(1){width:40px}
.menu-icon span:nth-child(2){width:64px}
.menu-icon span:nth-child(3){width:64px}

/* hero */
.hero{left:0;top:115px;width:1200px;height:565px;background:linear-gradient(100deg,#d8c9bd 0%,#cbb6a6 45%,#a8877a 75%,#6f5247 100%)}
.hero-title{left:87px;top:305px;font-family:"Roboto",sans-serif;font-weight:700;font-size:48px;color:var(--white);letter-spacing:.5px}
.hero-sub{left:87px;top:366px;font-family:"Lora",serif;font-size:27px;color:var(--text)}
.see-collection{left:87px;top:428px;width:149px;height:39px;font-size:13px}
.upload-rx{left:250px;top:428px;width:206px;height:39px;font-size:13px;background:rgba(255,255,255,.15);border:2px solid #c9ccce;color:#f2f2f2}

/* welcome */
.section-title{font-family:"Oswald",sans-serif;font-weight:400;font-size:32px;color:#222}
.section-title em{font-style:normal;color:var(--blue)}
.welcome-title{left:87px;top:740px}
.welcome-text{left:87px;top:807px;width:531px;font-size:13px;line-height:23.5px;color:var(--muted);text-align:justify}
.read-more{left:87px;top:1010px;width:105px;height:36px;font-size:12px}
.welcome-photos{left:673px;top:751px;width:440px;height:295px;display:flex}
.welcome-photos div{flex:1}

/* featured */
.featured-title{left:0;width:1200px;top:1107px;text-align:center}
.underline{position:absolute;height:2px;background:var(--blue);width:60px;border-radius:1px}
.cards{position:absolute;left:87px;top:1184px;width:1026px;display:grid;grid-template-columns:repeat(3,323px);grid-auto-rows:332px;column-gap:28.5px;row-gap:34px}
.card{position:relative;border:1px solid var(--line);background:var(--white)}
.lens-shot{position:absolute;left:50%;transform:translateX(-50%);top:18px;width:150px;height:130px;border-radius:8px;background:radial-gradient(ellipse at center,#eef3f6 0%,#dfe7ec 55%,#ffffff 100%)}
.lens-shot.tint{background:radial-gradient(ellipse at center,#e2f0fb 0%,#d2e6f4 55%,#ffffff 100%)}
.card-title{position:absolute;left:0;right:0;top:178px;text-align:center;font-size:16.5px;font-weight:500;color:#222;text-transform:uppercase}
.card-text{position:absolute;left:28px;right:28px;top:210px;text-align:center;font-size:12.5px;line-height:23px;color:var(--muted)}
.card-foot{position:absolute;left:-1px;right:-1px;bottom:-1px;height:46px;display:flex;color:var(--white);font-size:17px}
.price{width:146px;background:var(--slate);display:flex;align-items:center;justify-content:center}
.order{flex:1;background:var(--blue);display:flex;align-items:center;justify-content:center;text-transform:uppercase}

/* designer blocks */
.glasses-photo{left:0;top:2322px;width:600px;height:403px;background:linear-gradient(135deg,#e8e4dc 0%,#cfd6d6 50%,#8fa5a4 100%)}
.glasses-panel{left:463px;top:2368px;width:650px;height:314px;background:var(--slate)}
.panel-title{position:absolute;left:25px;top:38px;font-family:"Oswald",sans-serif;font-size:30px;color:var(--white)}
.panel-line{left:25px;top:93px;background:#8fc9f2}
.panel-text{position:absolute;left:25px;top:108px;width:600px;font-size:12.5px;line-height:23.5px;color:#e6e9ec;text-align:justify}
.panel-btn{left:25px;top:230px;width:112px;height:37px;font-size:12px}
.sun-photo{left:602px;top:2727px;width:598px;height:378px;background:linear-gradient(120deg,#c9b8ae 0%,#9c8478 45%,#4a4a55 100%)}
.sun-title{left:85px;top:2790px}
.sun-line{left:85px;top:2846px}
.sun-text{left:85px;top:2862px;width:489px;font-size:13px;line-height:23.5px;color:var(--muted);text-align:justify}
.sun-btn{left:85px;top:3009px;width:113px;height:37px;font-size:12px}

/* footer */
.site-footer{left:0;top:3174px;width:1200px;height:206px;background:var(--navy)}
.foot-head{position:absolute;top:26px;font-family:"Roboto",sans-serif;font-weight:700;font-size:19px;color:var(--white)}
.cat-list{position:absolute;top:70px;list-style:none;font-size:12.5px;color:#dfe5ec;line-height:27.3px;text-transform:uppercase}
.newsletter{position:absolute;left:671px;top:70px;width:442px;height:44px;display:flex}
.newsletter .field{flex:1;background:#5e6a7a;color:#e5e9ee;font-size:13px;display:flex;align-items:center;padding-left:12px}
.newsletter .submit{width:110px;background:var(--blue);color:var(--white);font-weight:500;font-size:15px;display:flex;align-items:center;justify-content:center}
.social{position:absolute;top:150px;width:30px;height:30px;border:2px solid #c9d0d8;border-radius:50%}
.bottom-bar{left:0;top:3380px;width:1200px;height:55px;background:var(--footer-bar)}
.copyright{position:absolute;left:87px;top:20px;font-size:12px;color:#d7dbdf}
.pay{position:absolute;top:17px;width:44px;height:22px;background:#c8ccd0;border-radius:3px}
</style>
</head>
<body>

<header class="site-header">
  <div class="abs phone-icon">
    <svg width="22" height="22" viewBox="0 0 24 24"><path d="M6.6 10.8c1.4 2.8 3.8 5.1 6.6 6.6l2.2-2.2c.3-.3.7-.4 1-.2 1.1.4 2.3.6 3.6.6.6 0 1 .4 1 1V20c0 .6-.4 1-1 1C10.6 21 3 13.4 3 4c0-.6.4-1 1-1h3.5c.6 0 1 .4 1 1 0 1.3.2 2.5.6 3.6.1.3 0 .7-.2 1L6.6 10.8z" fill="#333a40"/></svg>
  </div>
  <div class="abs phone-number">555-0142-888</div>
  <div class="abs brand">Glintwell</div>
  <div class="abs login">LOGIN</div>
  <div class="btn header-order">Order Now</div>
  <div class="abs menu-icon"><span></span><span></span><span></span></div>
</header>

<section class="abs hero" role="img" aria-label="Woman adjusting her eyeglasses against a soft beige backdrop"></section>
<h1 class="abs hero-title">WE ARE DIFFEREN</h1>
<p class="abs hero-sub">We offer same day service or next day shipping.</p>
<div class="btn see-collection">See Collection</div>
<div class="btn upload-rx">Upload Prescription</div>

<h2 class="abs section-title welcome-title">Welcome to <em>Glintwell</em></h2>
<p class="abs welcome-text">Lorem Ipsum is simply dummy text of the printing and typesetting industry. Lorem Ipsum has been the industry's standard dummy text ever since the 1500s, when an unknown printer took a galley of type and scrambled it to make a type specimen book. It has survived not only five centuries, but also the leap into electronic typesetting, remaining essentially unchanged. It was popularised in the 1960s with the release of Letraset sheets containing Lorem Ipsum passages, and more recently with desktop publishing software like Aldus PageMaker including versions of Lorem Ipsum more recently with desktop publishing software like Aldus PageMaker more recently with desktop publishing software l</p>
<div class="btn read-more">Read More</div>
<div class="abs welcome-photos">
  <div role="img" aria-label="Woman in glasses holding a book" style="background:linear-gradient(160deg,#8a8f8c,#4a4f4d)"></div>
  <div role="img" aria-label="Smiling woman wearing glasses" style="background:linear-gradient(160deg,#b9c7d3,#6f8aa6)"></div>
  <div role="img" aria-label="Woman wearing fashion glasses" style="background:linear-gradient(160deg,#c9b39c,#7a5e4a)"></div>
</div>

<h2 class="abs section-title featured-title">Featured <em>Glasses</em></h2>
<div class="underline" style="left:570px;top:1157px"></div>

<section class="cards">
  <article class="card"><div class="lens-shot" role="img" aria-label="Single vision lens"></div><h3 class="card-title">Single Vision Lenses</h3><p class="card-text">Lorem Ipsum is simply dummy text of the printing and typesetting industry.Lorem</p><div class="card-foot"><span class="price">$79</span><span class="order">Order Now</span></div></article>
  <article class="card"><div class="lens-shot" role="img" aria-label="High index lens"></div><h3 class="card-title">High Index Lenses</h3><p class="card-text">Lorem Ipsum is simply dummy text of the printing and typesetting industry.Lorem</p><div class="card-foot"><span class="price">$179</span><span class="order">Order Now</span></div></article>
  <article class="card"><div class="lens-shot tint" role="img" aria-label="Reading lens"></div><h3 class="card-title">Reading Lenses</h3><p class="card-text">Lorem Ipsum is simply dummy text of the printing and typesetting industry.Lorem</p><div class="card-foot"><span class="price">$79</span><span class="order">Order Now</span></div></article>
  <article class="card"><div class="lens-shot" role="img" aria-label="Single vision lens"></div><h3 class="card-title">Single Vision Lenses</h3><p class="card-text">Lorem Ipsum is simply dummy text of the printing and typesetting industry.Lorem</p><div class="card-foot"><span class="price">$79</span><span class="order">Order Now</span></div></article>
  <article class="card"><div class="lens-shot" role="img" aria-label="High index lens"></div><h3 class="card-title">High Index Lenses</h3><p class="card-text">Lorem Ipsum is simply dummy text of the printing and typesetting industry.Lorem</p><div class="card-foot"><span class="price">$179</span><span class="order">Order Now</span></div></article>
  <article class="card"><div class="lens-shot tint" role="img" aria-label="Reading lens"></div><h3 class="card-title">Reading Lenses</h3><p class="card-text">Lorem Ipsum is simply dummy text of the printing and typesetting industry.Lorem</p><div class="card-foot"><span class="price">$79</span><span class="order">Order Now</span></div></article>
  <article class="card"><div class="lens-shot" role="img" aria-label="Single vision lens"></div><h3 class="card-title">Single Vision Lenses</h3><p class="card-text">Lorem Ipsum is simply dummy text of the printing and typesetting industry.Lorem</p><div class="card-foot"><span class="price">$79</span><span class="order">Order Now</span></div></article>
  <article class="card"><div class="lens-shot" role="img" aria-label="High index lens"></div><h3 class="card-title">High Index Lenses</h3><p class="card-text">Lorem Ipsum is simply dummy text of the printing and typesetting industry.Lorem</p><div class="card-foot"><span class="price">$179</span><span class="order">Order Now</span></div></article>
  <article class="card"><div class="lens-shot tint" role="img" aria-label="Reading lens"></div><h3 class="card-title">Reading Lenses</h3><p class="card-text">Lorem Ipsum is simply dummy text of the printing and typesetting industry.Lorem</p><div class="card-foot"><span class="price">$79</span><span class="order">Order Now</span></div></article>
</section>

<div class="abs glasses-photo" role="img" aria-label="Smiling man in glasses leaning on a desk in a bright studio"></div>
<section class="abs glasses-panel">
  <h2 class="panel-title">Designer Glasses</h2>
  <div class="underline panel-line"></div>
  <p class="panel-text">Lorem Ipsum is simply dummy text of the printing and typesetting industry. Lorem Ipsum has been the industry's standard dummy text ever since the 1500s, when an unknown printer took a galley of type and scrambled it to make a type specimen book. It has survived not only five centuries, but also the leap into electronic typesetting, remaining essentially unchanged. It was popularised in the</p>
  <div class="btn panel-btn">Shop Now</div>
</section>

<h2 class="abs section-title sun-title">Designer Sunglasses</h2>
<div class="underline sun-line"></div>
<p class="abs sun-text">Lorem Ipsum is simply dummy text of the printing and typesetting industry. Lorem Ipsum has been the industry's standard dummy text ever since the 1500s, when an unknown printer took a galley of type and scrambled it to make a type specimen book. It has survived not only five centuries, but also the leap into electronic typesetting, remaining essentially unchanged. It was popularised in the</p>
<div class="btn sun-btn">Shop Now</div>
<div class="abs sun-photo" role="img" aria-label="Woman in sunglasses and a beanie sitting by the sea"></div>

<footer class="abs site-footer">
  <h4 class="foot-head" style="left:87px">CATEGORIES</h4>
  <ul class="cat-list" style="left:87px">
    <li>Single Vision Lenses</li><li>High Index Lenses</li><li>Reading Lenses</li><li>Digital HD Progressive Lenses</li>
  </ul>
  <ul class="cat-list" style="left:348px">
    <li>RX &amp; Non-RX Sunglasses</li><li>RX &amp; Non-RX Polarized Sunglasses</li><li>Computer Lenses- Transition Lenses</li><li>Bi-Focal Lenses</li>
  </ul>
  <h4 class="foot-head" style="left:671px">NEWSLETTER</h4>
  <div class="newsletter"><span class="field">Your Email</span><span class="submit">SUBMIT</span></div>
  <span class="social" style="left:995px"></span>
  <span class="social" style="left:1038px"></span>
  <span class="social" style="left:1083px"></span>
</footer>

<div class="abs bottom-bar">
  <span class="copyright">2017 Glintwell. All Rights Reserved.</span>
  <span class="pay" style="left:818px"></span>
  <span class="pay" style="left:876px"></span>
  <span class="pay" style="left:934px"></span>
  <span class="pay" style="left:992px"></span>
  <span class="pay" style="left:1050px;width:63px"></span>
</div>

</body>
</html>
```